Business Card Design

We need a new buisness card designed for a new company in Darwin
We dig trenchs and lay pipes for the communication industry,Electrical industry, Teleco industry,
We also do some concrete works as well,
And small excavation work
Industry/Entity Type
Communication
Contact Information for Business Card
Tolvani Contracting PTY LTD
Pit and Pipe installations
Trenching,Excavations, Concreting ,
civil works, unistrut soloutions ,over thirty years experiance
WHERE NOT FAZED WE WILL LAY ANYTHING
Contact Glen 0451936024 ps
(would like name to stand out somehow in another text or graphic sort of a way am also looking for some sort of slogan) will most likely be a red card with black writing

```html
<!DOCTYPE html>
<html lang="en">
<head>
<meta charset="utf-8">
<title>Tolvani Contracting – Business Card</title>
<link rel="stylesheet" href="https://fonts.googleapis.com/css2?family=Roboto+Condensed:wght@700&family=Roboto:wght@300;700&display=swap">
<style>
  :root {
    --backdrop: #3c3c3d;
    --card: #f5f6f5;
    --name-red: #860b15;
    --ink-grey: #55565a;
    --copy-grey: #68696c;
    --band-top: #c4171f;
    --band-bottom: #640007;
    --white: #ffffff;
  }
  * { margin: 0; padding: 0; box-sizing: border-box; }
  html, body {
    width: 1200px;
    height: 999px;
    overflow: hidden;
    background: var(--backdrop);
  }
  .card {
    position: absolute;
    left: 75px;
    top: 200px;
    width: 1050px;
    height: 599px;
    background: var(--card);
    text-align: center;
  }
  .contact-name {
    position: absolute;
    top: 66px;
    width: 100%;
    font-family: "Roboto Condensed", "Arial Narrow", sans-serif;
    font-weight: 700;
    font-size: 76px;
    line-height: 1;
    color: var(--name-red);
  }
  .contact-phone {
    position: absolute;
    top: 162px;
    width: 100%;
    font-family: "Roboto", Arial, sans-serif;
    font-weight: 700;
    font-size: 62px;
    line-height: 1;
    letter-spacing: -0.5px;
    color: var(--ink-grey);
  }
  .brand-band {
    position: absolute;
    top: 264px;
    left: 0;
    width: 100%;
    height: 111px;
    background: linear-gradient(to bottom, var(--band-top) 0%, #a8101a 45%, var(--band-bottom) 100%);
    display: flex;
    align-items: center;
    justify-content: center;
  }
  .company-name {
    font-family: "Roboto Condensed", "Arial Narrow", sans-serif;
    font-weight: 700;
    font-size: 86px;
    line-height: 1;
    color: var(--white);
    white-space: nowrap;
    margin-top: 6px;
  }
  .company-suffix {
    font-size: 36px;
    margin-left: 6px;
  }
  .slogan {
    position: absolute;
    top: 388px;
    width: 100%;
    font-family: "Roboto", Arial, sans-serif;
    font-weight: 700;
    font-size: 35px;
    line-height: 1;
    color: var(--ink-grey);
  }
  .services {
    position: absolute;
    top: 480px;
    width: 100%;
    font-family: "Roboto", Arial, sans-serif;
    font-weight: 300;
    font-size: 29px;
    line-height: 40px;
    color: var(--copy-grey);
  }
  .footer-band {
    position: absolute;
    left: 0;
    bottom: 0;
    width: 100%;
    height: 36px;
    background: linear-gradient(to bottom, var(--band-top) 0%, var(--band-bottom) 100%);
  }
</style>
</head>
<body>
  <div class="card">
    <div class="contact-name">GLEN</div>
    <div class="contact-phone">0451936024</div>
    <div class="brand-band">
      <div class="company-name">TOLVANI CONTRACTING<span class="company-suffix">PTY LTD</span></div>
    </div>
    <div class="slogan">WHERE NOT FAZED WE WILL LAY ANYTHING</div>
    <p class="services">Pit and Pipe installations Trenching,Excavations, concreting civil works,<br>over thirty years experiance</p>
    <div class="footer-band"></div>
  </div>
</body>
</html>
```